BUSINESS CARD DESIGN
TWQ ZL GROUP
I need single sided standard sized Business Card [3.5" x 2"]
USE WHAT LOOKS BEST
Professional
BENITO MALVEZ
PRESIDENT
2876 W. PINE LOOP 64, EDINBURG, TX 78590
BMALVEZ41@QUOMIBOX.COM

```html
<!DOCTYPE html>
<html lang="en">
<head>
<meta charset="utf-8">
<title>TWQ ZL GROUP – Business Card</title>
<link href="https://fonts.googleapis.com/css2?family=Arimo:wght@400;700&display=swap" rel="stylesheet">
<style>
  :root {
    --backdrop: #3b3d3f;
    --card: #ffffff;
    --brand-blue: #2a9fd6;
    --brand-green: #6dbb45;
    --ink: #666a6d;
    --rule: #c9cdd0;
  }
  * { margin: 0; padding: 0; box-sizing: border-box; }
  html, body {
    width: 1200px;
    height: 901px;
    overflow: hidden;
    background: var(--backdrop);
    font-family: "Arimo", Arial, sans-serif;
  }
  .card {
    position: absolute;
    left: 150px;
    top: 193px;
    width: 900px;
    height: 514px;
    background: var(--card);
    box-shadow: 0 10px 30px rgba(0,0,0,0.35);
  }
  .brand {
    position: absolute;
    left: 60px;
    top: 190px;
    width: 340px;
    display: flex;
    align-items: center;
    justify-content: center;
    gap: 16px;
  }
  .brand-dot {
    width: 26px;
    height: 26px;
    border-radius: 50%;
    background: var(--brand-green);
  }
  .brand-name {
    font-size: 68px;
    font-weight: 400;
    letter-spacing: 2px;
    color: var(--brand-green);
  }
  .divider {
    position: absolute;
    left: 440px;
    top: 120px;
    width: 1px;
    height: 290px;
    background: var(--rule);
  }
  .details {
    position: absolute;
    left: 482px;
    top: 130px;
    color: var(--ink);
  }
  .person-name {
    font-size: 30px;
    font-weight: 700;
    color: var(--brand-blue);
    line-height: 1.1;
  }
  .person-title {
    font-size: 22px;
    margin-top: 4px;
  }
  .address {
    font-size: 23px;
    line-height: 1.3;
    margin-top: 28px;
  }
  .contact {
    list-style: none;
    margin-top: 22px;
    font-size: 23px;
  }
  .contact li {
    display: flex;
    align-items: center;
    gap: 12px;
    line-height: 1.5;
  }
  .contact svg { flex: none; }
</style>
</head>
<body>
  <main class="card">
    <div class="brand">
      <span class="brand-dot"></span>
      <span class="brand-name">TWQZL</span>
    </div>

    <div class="divider"></div>

    <section class="details">
      <p class="person-name">Benito Malvez</p>
      <p class="person-title">President</p>
      <p class="address">2876 W. PINE LOOP 64<br>EDINBURG, TX 78590</p>
      <ul class="contact">
        <li>
          <svg width="20" height="22" viewBox="0 0 20 22" aria-label="Phone">
            <rect x="4" y="1" width="12" height="20" rx="2" fill="var(--brand-blue)"/>
            <rect x="6" y="4" width="8" height="12" fill="#fff"/>
            <circle cx="10" cy="18.5" r="1" fill="#fff"/>
          </svg>
          <span>956-418-3052</span>
        </li>
        <li>
          <svg width="22" height="16" viewBox="0 0 22 16" aria-label="Email">
            <rect x="1" y="1" width="20" height="14" fill="var(--brand-blue)"/>
            <path d="M1 1 L11 9 L21 1" fill="none" stroke="#fff" stroke-width="1.6"/>
          </svg>
          <span>bmalvez41@quomibox.com</span>
        </li>
      </ul>
    </section>
  </main>
</body>
</html>
```